RE Listing package
Listing flyer and brochure
Real Estate
Professional and elegant.
It must be somewhat similar to our postcard project that closed on 12/26. We're really looking to be able to brand ourselves and become recognizable with all our marketing.

```html
<!DOCTYPE html>
<html lang="en">
<head>
<meta charset="utf-8">
<title>Listing Flyer – 4182 Maple Crest Lane</title>
<link rel="stylesheet" href="https://fonts.googleapis.com/css2?family=Cinzel:wght@600&family=Open+Sans:wght@400;600;800&family=Playfair+Display:ital,wght@1,800&display=swap">
<style>
  :root{
    --board:#f2f2f2;
    --ink:#222;
    --muted:#6b6b6b;
    --green-dark:#17713a;
    --green:#3c9a3f;
    --green-light:#7cc24f;
    --mint:#eef6e6;
    --blue:#1f6fb8;
    --blue-light:#3c97dc;
    --white:#fff;
  }
  *{box-sizing:border-box;margin:0;padding:0}
  html,body{width:1200px;height:947px;overflow:hidden;background:var(--board);font-family:"Open Sans",Arial,sans-serif;color:var(--ink)}
  .board{position:relative;width:1200px;height:947px}
  .board-title{position:absolute;top:22px;left:0;width:100%;text-align:center;font-size:34px;font-weight:400;color:#555}
  .page{position:absolute;width:525px;height:375px;background:var(--white);overflow:hidden;box-shadow:0 1px 4px rgba(0,0,0,.18)}
  .row-1{top:92px}.row-2{top:500px}
  .col-front{left:68px}.col-back{left:608px}

  /* front */
  .front-header{position:absolute;top:0;left:0;width:100%;height:46px;background:linear-gradient(90deg,var(--green-dark),var(--green) 60%,var(--green-light));display:flex;align-items:center;padding-left:26px}
  .address{font-family:"Cinzel",Georgia,serif;font-weight:600;font-size:22px;color:var(--white);letter-spacing:.3px}
  .house-photo{position:absolute;top:46px;left:0;width:100%;height:258px;background:linear-gradient(180deg,#8fb7dc 0%,#b9cfe0 30%,#cbb79a 55%,#a88e6b 78%,#5f7a45 100%)}
  .agents-photo{position:absolute;top:120px;left:290px;width:130px;height:184px;background:linear-gradient(180deg,#4a3b33 0%,#6a5a55 40%,#2f3f5e 100%)}
  .price-badge{position:absolute;top:60px;left:0;width:100px;height:100px}
  .price-text{position:absolute;top:88px;left:14px;color:var(--white);line-height:1.1}
  .price-text .label{display:block;font-size:15px;font-weight:600}
  .price-text .amount{display:block;font-size:11px}
  .swoosh{position:absolute;top:268px;left:0;width:525px;height:50px}
  .front-footer{position:absolute;left:0;bottom:0;width:100%;height:62px;display:flex;align-items:center;padding:0 18px;gap:14px}
  .phone{font-weight:800;font-size:25px;letter-spacing:-.3px}
  .website{font-weight:800;font-size:13px;letter-spacing:.2px}
  .brand{margin-left:auto;display:flex;flex-direction:column;align-items:center;gap:2px}
  .brand-dot{width:18px;height:18px;border-radius:50%;background:var(--green)}
  .brand-name{font-size:7px;font-weight:600;color:var(--green-dark)}

  /* back */
  .back{background:linear-gradient(160deg,var(--white) 55%,var(--mint) 80%,#d3eabf 100%)}
  .back-edge{position:absolute;left:0;bottom:0;width:525px;height:375px}
  .headline{position:absolute;top:10px;left:0;width:100%;text-align:center;font-family:"Playfair Display",Georgia,serif;font-style:italic;font-weight:800;font-size:21px;color:var(--green)}
  .description{position:absolute;top:44px;left:22px;width:481px;display:grid;grid-template-columns:1fr 1fr;gap:16px;font-size:7.4px;line-height:1.35}
  .gallery{position:absolute;top:150px;left:22px;width:481px;height:128px;display:grid;grid-template-columns:2fr 1fr 1fr 1fr;grid-template-rows:1fr 1fr;gap:5px}
  .gallery .photo{background:linear-gradient(135deg,#c9b08a,#8a6b4a)}
  .gallery .photo.lead{grid-row:span 2;background:linear-gradient(180deg,#9ab6cf,#c2ad8b 55%,#6d7f4d)}
  .gallery .photo.cool{background:linear-gradient(135deg,#d8d2c4,#9b8f7b)}
  .disclaimer{position:absolute;top:287px;left:40px;width:445px;text-align:center;font-size:6px;line-height:1.3;color:var(--muted)}
  .rule{position:absolute;top:318px;left:22px;width:481px;height:2px;background:var(--green)}
  .license{position:absolute;top:326px;left:0;width:100%;text-align:center;font-family:"Cinzel",Georgia,serif;font-weight:600;font-size:12px;letter-spacing:.4px}
  .contact-line{position:absolute;top:346px;left:0;width:100%;text-align:center;font-size:6.5px;color:var(--muted);letter-spacing:.3px}
</style>
</head>
<body>
<main class="board">
  <h1 class="board-title">Flyer</h1>

  <!-- front, version A -->
  <section class="page front row-1 col-front">
    <header class="front-header"><span class="address">4182 Maple Crest Lane, Oak Hollow</span></header>
    <div class="house-photo" role="img" aria-label="Two-storey stucco home with tiled roof and landscaped front yard"></div>
    <div class="agents-photo" role="img" aria-label="Listing agents standing together"></div>
    <svg class="price-badge" viewBox="0 0 100 100" aria-hidden="true"><path d="M0 0 H55 A45 45 0 0 1 55 100 H0 Z" fill="var(--blue)"/><path d="M0 6 H52 A39 39 0 0 1 52 94 H0" fill="none" stroke="var(--blue-light)" stroke-width="2"/></svg>
    <p class="price-text"><span class="label">List Price</span><span class="amount">$799,000</span></p>
    <svg class="swoosh" viewBox="0 0 525 50" preserveAspectRatio="none" aria-hidden="true"><path d="M0 40 Q260 -6 525 20 V50 H0 Z" fill="var(--green)"/><path d="M0 46 Q260 6 525 30 V50 H0 Z" fill="var(--white)"/></svg>
    <footer class="front-footer">
      <span class="phone">(555) 201-4478</span>
      <span class="website">WWW.DORRANPELSEY.COM</span>
      <span class="brand"><span class="brand-dot"></span><span class="brand-name">Linden &amp; Associates</span></span>
    </footer>
  </section>

  <!-- back, version A -->
  <section class="page back row-1 col-back">
    <svg class="back-edge" viewBox="0 0 525 375" aria-hidden="true"><path d="M0 300 Q120 330 0 375 Z" fill="var(--green-light)" opacity=".35"/></svg>
    <h2 class="headline">Simply Stunning Home In Briarwood Estates!</h2>
    <div class="description">
      <p>Gorgeous 5 bedroom &amp; 3.5 bathroom, 3,652 square foot home in Briarwood Estates! Beautiful features, upgrades and decorator amenities throughout. Stone walk way leads to an inviting entrance, front door opens to travertine flooring and high ceilings, living room and formal dining room feature a two way fireplace, large kitchen with granite counter tops, recessed lighting, double ovens,</p>
      <p>cook top, built-in microwave, eat-in kitchen area open to the family room with fireplace, recessed lighting and custom built-in wall unit, one bedroom with private bathroom downstairs, large master suite, master bathroom with jetted tub, tile flooring, three additional bedrooms upstairs, laundry room and nook area. Backyard features a BBQ area, fire pit, and space to entertain.</p>
    </div>
    <div class="gallery">
      <div class="photo lead" role="img" aria-label="Rear yard and patio"></div>
      <div class="photo" role="img" aria-label="Living room"></div>
      <div class="photo cool" role="img" aria-label="Kitchen"></div>
      <div class="photo" role="img" aria-label="Dining room"></div>
      <div class="photo cool" role="img" aria-label="Master bathroom"></div>
      <div class="photo" role="img" aria-label="Family room"></div>
      <div class="photo cool" role="img" aria-label="Bedroom"></div>
    </div>
    <p class="disclaimer">Information deemed reliable but not guaranteed. Buyer to verify all details. Offer subject to change without notice.</p>
    <div class="rule"></div>
    <p class="license">BROKER / MAKELAR BRE LICENSE # 02918374</p>
    <p class="contact-line">EMAIL: INFO@LINDENASSOCIATES.COM · WEBSITE: WWW.DORRANPELSEY.COM</p>
  </section>

  <!-- front, version B -->
  <section class="page front row-2 col-front">
    <header class="front-header"><span class="address">4182 Maple Crest Lane, Oak Hollow</span></header>
    <div class="house-photo" role="img" aria-label="Two-storey stucco home with tiled roof and landscaped front yard"></div>
    <div class="agents-photo" role="img" aria-label="Listing agents standing together"></div>
    <svg class="price-badge" viewBox="0 0 100 100" aria-hidden="true"><path d="M0 0 H55 A45 45 0 0 1 55 100 H0 Z" fill="var(--blue)"/><path d="M0 6 H52 A39 39 0 0 1 52 94 H0" fill="none" stroke="var(--blue-light)" stroke-width="2"/></svg>
    <p class="price-text"><span class="label">List Price</span><span class="amount">$799,000</span></p>
    <svg class="swoosh" viewBox="0 0 525 50" preserveAspectRatio="none" aria-hidden="true"><path d="M0 40 Q260 -6 525 20 V50 H0 Z" fill="var(--green)"/><path d="M0 46 Q260 6 525 30 V50 H0 Z" fill="var(--white)"/></svg>
    <footer class="front-footer">
      <span class="phone">(555) 306-7712</span>
      <span class="website">WWW.DORRANPELSEY.COM</span>
      <span class="brand"><span class="brand-dot"></span><span class="brand-name">Linden &amp; Associates</span></span>
    </footer>
  </section>

  <!-- back, version B -->
  <section class="page back row-2 col-back">
    <svg class="back-edge" viewBox="0 0 525 375" aria-hidden="true"><path d="M0 300 Q120 330 0 375 Z" fill="var(--green-light)" opacity=".35"/></svg>
    <h2 class="headline">Simply Stunning Home In Briarwood Estates!</h2>
    <div class="description">
      <p>Gorgeous 5 bedroom &amp; 3.5 bathroom, 3,652 square foot home in Briarwood Estates! Beautiful features, upgrades and decorator amenities throughout. Stone walk way leads to an inviting entrance, front door opens to travertine flooring and high ceilings, living room and formal dining room feature a two way fireplace, large kitchen with granite counter tops, recessed lighting, double ovens,</p>
      <p>cook top, built-in microwave, eat-in kitchen area open to the family room with fireplace, recessed lighting and custom built-in wall unit, one bedroom with private bathroom downstairs, large master suite, master bathroom with jetted tub, tile flooring, three additional bedrooms upstairs, laundry room and nook area. Backyard features a BBQ area, fire pit, and space to entertain.</p>
    </div>
    <div class="gallery">
      <div class="photo lead" role="img" aria-label="Rear yard and patio"></div>
      <div class="photo" role="img" aria-label="Living room"></div>
      <div class="photo cool" role="img" aria-label="Kitchen"></div>
      <div class="photo" role="img" aria-label="Dining room"></div>
      <div class="photo cool" role="img" aria-label="Master bathroom"></div>
      <div class="photo" role="img" aria-label="Family room"></div>
      <div class="photo cool" role="img" aria-label="Bedroom"></div>
    </div>
    <p class="disclaimer">Information deemed reliable but not guaranteed. Buyer to verify all details. Offer subject to change without notice.</p>
    <div class="rule"></div>
    <p class="license">OWEN MARSH REAL ESTATE BRE LICENSE # 02735160</p>
    <p class="contact-line">EMAIL: INFO@LINDENASSOCIATES.COM · WEBSITE: WWW.DORRANPELSEY.COM</p>
  </section>
</main>
</body>
</html>
```